Cedar Ridge Planting Works and Sun-Sprout Megamart

The billboard will be on highway frontage and located directly next to my business building the marketing is for. The marketing on the billboard will be more directed towards the sun-sprouts megamart service being provided. And since the sign is on the businesses property it will need to say, "Exit Right Now" along with an arrow pointing to the right when facing the sign.

```html
<!DOCTYPE html>
<html lang="en">
<head>
<meta charset="utf-8">
<title>Cedar Ridge Planting Works – Exit Right Now Billboard</title>
<link rel="stylesheet" href="https://fonts.googleapis.com/css2?family=Montserrat:wght@600;900&display=swap">
<style>
  :root {
    --page: #eef0f2;
    --panel-black: #1a1a1a;
    --grass-green: #6fae35;
    --grass-dark: #4f8a24;
    --frame-white: #ffffff;
    --brand-green: #86c23f;
    --headline: #ffffff;
    --headline-shadow: #1f3a10;
  }
  html, body {
    margin: 0;
    padding: 0;
    width: 1200px;
    height: 800px;
    overflow: hidden;
    background: var(--page);
  }
  .billboard {
    position: absolute;
    left: 20px;
    top: 140px;
    width: 1160px;
    height: 520px;
    display: block;
  }
  .brand-name {
    font-family: "Montserrat", sans-serif;
    font-weight: 600;
    fill: var(--brand-green);
  }
  .headline {
    font-family: "Montserrat", sans-serif;
    font-weight: 900;
    fill: var(--headline);
  }
  .headline-shadow {
    font-family: "Montserrat", sans-serif;
    font-weight: 900;
    fill: var(--headline-shadow);
    opacity: 0.55;
  }
</style>
</head>
<body>
<svg class="billboard" viewBox="0 0 1160 520" xmlns="http://www.w3.org/2000/svg">
  <defs>
    <linearGradient id="grass-fill" x1="0" y1="0" x2="1" y2="1">
      <stop offset="0" stop-color="#7cbc3c"/>
      <stop offset="1" stop-color="#5c9a2a"/>
    </linearGradient>
    <linearGradient id="sprout-strip" x1="0" y1="0" x2="0" y2="1">
      <stop offset="0" stop-color="#6b5a3a"/>
      <stop offset="0.5" stop-color="#5f8f2e"/>
      <stop offset="1" stop-color="#3e3526"/>
    </linearGradient>
    <radialGradient id="microgreens-tone" cx="0.5" cy="0.45" r="0.6">
      <stop offset="0" stop-color="#9a3b5c"/>
      <stop offset="0.5" stop-color="#3b4a2c"/>
      <stop offset="1" stop-color="#1c1c1c"/>
    </radialGradient>
    <radialGradient id="burger-tone" cx="0.6" cy="0.45" r="0.65">
      <stop offset="0" stop-color="#b07a45"/>
      <stop offset="0.6" stop-color="#5a3a25"/>
      <stop offset="1" stop-color="#2b1e16"/>
    </radialGradient>
    <radialGradient id="salad-tone" cx="0.5" cy="0.5" r="0.6">
      <stop offset="0" stop-color="#c97a2a"/>
      <stop offset="0.45" stop-color="#3f5a2a"/>
      <stop offset="1" stop-color="#1e1e1e"/>
    </radialGradient>
    <radialGradient id="juice-tone" cx="0.5" cy="0.5" r="0.6">
      <stop offset="0" stop-color="#3f9a3a"/>
      <stop offset="0.5" stop-color="#6a4e32"/>
      <stop offset="1" stop-color="#3a2a1e"/>
    </radialGradient>
  </defs>

  <!-- backdrop strip behind the photo tiles -->
  <rect class="sprout-strip" x="470" y="0" width="690" height="520" fill="url(#sprout-strip)" role="img" aria-label="Close-up of sprouting seedlings on a wooden board"/>

  <!-- photo tiles -->
  <g class="photo-grid">
    <rect x="616" y="0" width="544" height="520" fill="var(--frame-white)"/>
    <rect class="photo-tile" x="622" y="0" width="166" height="238" fill="url(#microgreens-tone)" role="img" aria-label="Pink-stemmed microgreens in a dark bowl"/>
    <rect class="photo-tile" x="796" y="0" width="364" height="238" fill="url(#burger-tone)" role="img" aria-label="Burger topped with microgreens on a plate"/>
    <rect class="photo-tile" x="622" y="246" width="306" height="274" fill="url(#salad-tone)" role="img" aria-label="Fresh salad with squash, mozzarella and greens"/>
    <rect class="photo-tile" x="936" y="246" width="224" height="274" fill="url(#juice-tone)" role="img" aria-label="Glass of green juice on a wooden board"/>
  </g>

  <!-- green arrow panel -->
  <polygon class="arrow-frame" points="196,0 486,0 578,260 486,520 196,520 262,260" fill="var(--frame-white)"/>
  <polygon class="arrow-panel" points="206,0 478,0 566,260 478,520 206,520 272,260" fill="url(#grass-fill)"/>

  <!-- black brand panel -->
  <polygon class="brand-panel" points="0,0 196,0 262,260 196,520 0,520" fill="var(--panel-black)"/>

  <!-- brand name -->
  <g class="brand">
    <circle cx="112" cy="196" r="14" fill="var(--brand-green)"/>
    <text class="brand-name" x="112" y="252" font-size="26" text-anchor="middle">Cedar Ridge</text>
    <text class="brand-name" x="112" y="284" font-size="20" text-anchor="middle">Planting Works</text>
  </g>

  <!-- headline -->
  <g class="headline-group">
    <text class="headline-shadow" x="396" y="168" font-size="112" text-anchor="middle" textLength="214" lengthAdjust="spacingAndGlyphs">EXIT</text>
    <text class="headline-shadow" x="396" y="276" font-size="100" text-anchor="middle" textLength="224" lengthAdjust="spacingAndGlyphs">RIGHT</text>
    <text class="headline-shadow" x="396" y="388" font-size="112" text-anchor="middle" textLength="220" lengthAdjust="spacingAndGlyphs">NOW</text>

    <text class="headline" x="392" y="164" font-size="112" text-anchor="middle" textLength="214" lengthAdjust="spacingAndGlyphs">EXIT</text>
    <text class="headline" x="392" y="272" font-size="100" text-anchor="middle" textLength="224" lengthAdjust="spacingAndGlyphs">RIGHT</text>
    <text class="headline" x="392" y="384" font-size="112" text-anchor="middle" textLength="220" lengthAdjust="spacingAndGlyphs">NOW</text>
  </g>
</svg>
</body>
</html>
```